Global Developmental Delay Awareness Day Poster

I need a poster to raise awareness for a condition called Global Developmental Delay (GDD) . The day of awareness for this condition is May 1. The condition is something found in children who are significantly delayed in their milestones. We are hopeful that through education and support more children with this condition can gain access to therapies and support to minimize the long term effects and maxamise their potential. Theme for GDD awareness is yellow so lots of yellow needed. Can be any yellow. Like it to be colourful, but not bright if that makes sense. I'd like it to be classy but fun and childish - this is a childhood diagnosis. Just not 'tacky'. Like the design to reflect the wonders of childhood so feel free to use your imagination!

Target Market(s)

Mums (and dads) of young children under 5

Colors
fee18a
fbf289

Requirements
Must have
• cheery, childish, happy feel - see uploaded poster examples for ideas. They are just ideas for theme. Different fun, childish fonts and 'sections' - perhaps with different colour backgrounds etc.
• Heading should be "Global Developmental Delay" or something similar
• Must have text as in the attachment
• Must have yellow 'theme'
• more colours than just yellow.
Nice to have
• colors - not bright but colorful.

```html
<!DOCTYPE html>
<html lang="en">
<head>
<meta charset="UTF-8">
<title>Global Developmental Delay Awareness</title>
<link rel="stylesheet" href="https://fonts.googleapis.com/css2?family=Fredoka:wght@600;700&family=Baloo+2:wght@600;700;800&display=swap">
<style>
  :root{
    --sky:#3aa2e6;
    --sky-deep:#1f7fcf;
    --sky-light:#6cc3f2;
    --navy:#1d2d6b;
    --ink:#1c2a66;
    --paper:#fbf289;
    --paper-edge:#fee18a;
    --coral:#ef6a6a;
    --coral-text:#ee5f6c;
    --orange:#f6821f;
    --cyan:#2db6ee;
    --purple:#c63be0;
    --white:#ffffff;
  }
  *{margin:0;padding:0;box-sizing:border-box;}
  html,body{width:848px;height:1200px;overflow:hidden;}
  body{font-family:"Baloo 2",sans-serif;color:var(--ink);}
  .poster{
    position:relative;width:848px;height:1200px;overflow:hidden;
    background:
      radial-gradient(ellipse at 30% 20%,var(--sky-light) 0%,transparent 55%),
      radial-gradient(ellipse at 80% 80%,var(--sky-light) 0%,transparent 50%),
      linear-gradient(160deg,var(--sky) 0%,var(--sky-deep) 60%,var(--sky) 100%);
  }
  .title{
    position:absolute;left:0;right:0;top:22px;text-align:center;z-index:5;
    font-family:"Fredoka",sans-serif;font-weight:700;color:var(--white);
    line-height:76px;letter-spacing:-2.5px;
    -webkit-text-stroke:14px var(--navy);paint-order:stroke fill;
    text-shadow:0 6px 0 var(--navy);
  }
  .title .line1,.title .line2{display:block;font-size:88px;}
  .character{position:absolute;z-index:1;border-radius:36px 36px 12px 12px;}
  .card{
    position:absolute;z-index:2;background:var(--paper);border-radius:14px;
    box-shadow:5px 6px 0 var(--navy);
  }
  .card p{font-weight:700;font-size:18px;line-height:22px;letter-spacing:-0.2px;}
  .tab{
    position:absolute;z-index:3;border:4px solid var(--paper-edge);border-radius:10px;
    color:var(--white);font-family:"Fredoka",sans-serif;font-weight:700;
    font-size:29px;display:flex;align-items:center;justify-content:center;
    text-shadow:1px 2px 0 rgba(29,45,107,.35);white-space:nowrap;
  }
  .tab-what{left:69px;top:272px;width:212px;height:62px;background:var(--coral);}
  .tab-causes{left:479px;top:270px;width:296px;height:66px;background:var(--orange);font-size:28px;}
  .tab-concern{left:45px;top:736px;width:280px;height:48px;background:var(--cyan);font-size:25px;justify-content:flex-start;padding-left:12px;}
  .tab-do{left:181px;top:947px;width:278px;height:46px;background:var(--purple);font-size:25px;justify-content:flex-start;padding-left:16px;}
  .card-what{left:86px;top:305px;width:335px;height:420px;padding:76px 16px 0 14px;}
  .card-causes{left:430px;top:305px;width:337px;height:420px;padding:44px 14px 0 16px;}
  .card-causes p{font-size:17px;line-height:20.5px;}
  .cause-list{list-style:none;margin:12px 0 10px;}
  .cause-list li{color:var(--coral-text);font-weight:800;font-size:21px;line-height:23px;padding-left:18px;position:relative;}
  .cause-list li::before{content:"";position:absolute;left:0;top:8px;width:9px;height:9px;border-radius:50%;background:var(--coral-text);}
  .card-concern{left:64px;top:751px;width:545px;height:178px;padding:42px 80px 0 34px;}
  .card-do{left:199px;top:956px;width:548px;height:176px;padding:48px 20px 0 29px;}
  .contact{
    position:absolute;left:28px;top:1160px;font-family:"Fredoka",sans-serif;font-weight:700;
    font-size:25px;color:var(--white);-webkit-text-stroke:5px var(--navy);paint-order:stroke fill;
  }
  .contact-field{position:absolute;left:522px;top:1158px;width:316px;height:32px;background:var(--white);}
  .kid-glasses{left:8px;top:163px;width:90px;height:212px;background:linear-gradient(#3d4aa0 0 30%,#f2c6a0 30% 60%,#ef5b3a 60% 80%,#7a4a2a 80%);}
  .kid-curly{left:735px;top:170px;width:95px;height:211px;background:linear-gradient(#5a3320 0 30%,#f6cfae 30% 60%,#49a3dc 60% 80%,#2c2c3a 80%);}
  .kid-pigtails{left:592px;top:747px;width:120px;height:222px;z-index:4;background:linear-gradient(#6b3a22 0 28%,#f9d7bd 28% 56%,#2aa35a 56% 78%,#9bcf4a 78%);}
  .kid-redtop{left:52px;top:943px;width:125px;height:215px;background:linear-gradient(#b0602c 0 30%,#f9d2b4 30% 58%,#e8373c 58% 76%,#f7d21b 76%);}
</style>
</head>
<body>
<main class="poster">
  <h1 class="title"><span class="line1">Global Developmental</span><span class="line2">Delay Awareness</span></h1>

  <div class="character kid-glasses" role="img" aria-label="Cartoon boy with glasses waving"></div>
  <div class="character kid-curly" role="img" aria-label="Cartoon boy with curly hair waving"></div>
  <div class="character kid-redtop" role="img" aria-label="Cartoon girl in red top waving"></div>

  <div class="tab tab-what">What is GDD?</div>
  <section class="card card-what">
    <p>Every child develops at her or his own pace. A developmental delay is more than being ‘a little behind.” It means your child is continually behind in skills other kids his age have.<br>Global developmental delay is diagnosed when a child is significantly delayed in two or more of the 5 developmental realms including Cognitive (or thinking), Social and emotional, Communication, Fine motor and Gross motor</p>
  </section>

  <div class="tab tab-causes">What causes GDD?</div>
  <section class="card card-causes">
    <p>There are many possible causes of global developmental delay. Some are permanent, but others aren’t. They include:</p>
    <ul class="cause-list">
      <li>Genetic conditions:</li>
      <li>Complications in pregnancy or birth:</li>
      <li>Environmental issues:</li>
      <li>Other medical conditions:</li>
    </ul>
    <p>More often than not a child received a secondary diagnosis as they grow such as intellectual disability or autism spectrum disorder, in which case the name for the disorder replaces the term developmental delay.</p>
  </section>

  <div class="tab tab-concern">If you are concerned</div>
  <section class="card card-concern">
    <p>Early intervention programs and therapies can give many children with global development delays a head start and allow them to reach their full potential. If you are concerned that your child is not developing at the rate you would expect, please talk to your GP.</p>
  </section>

  <div class="character kid-pigtails" role="img" aria-label="Cartoon girl with pigtails"></div>

  <div class="tab tab-do">What can you do?</div>
  <section class="card card-do">
    <p>Each child is different in their own wonderful way, if we choose to celebrate and understand the things that make us unique as well as the ones that bring us together, we can create a much happier and more inclusive environment for all our children.</p>
  </section>

  <div class="contact">Looking for more info or support contact:</div>
  <div class="contact-field"></div>
</main>
</body>
</html>
```